【依頼の目的/概要】
電子書籍(lumora)の表紙デザインをお願いします。

【画像サイズ】 ※RZBより抜粋
表紙ファイルの理想的な寸法 2,560×1,600ピクセルです。
注:画像の寸法は 1,000×625ピクセル以上であることが必要です。
画像の最大の寸法は 10,000×10,000ピクセルです。

【タイトル】

5つの航路・ヴォルテノ大年譜など
人類普遍の必読真理書をギュっと1冊にまとめました

【著者】

RUNO

【本の内容】

5つの航路・ヴォルテノ大年譜などの人間心理・成功本を
まとめて解説した本です。

※本文を参考資料として添付します。

【デザイン要望】

特にイメージにこだわりはありませんので、
自由な発送でのデザインご応募を楽しみにしています。

※次点の方への参加報酬を設定致しました。

※その他 必要な情報がありましたら、お問い合わせください。

```html
<!DOCTYPE html>
<html lang="ja">
<head>
<meta charset="utf-8">
<title>5つの航路 ヴォルテノ大年譜など — RUNO</title>
<link href="https://fonts.googleapis.com/css2?family=Noto+Sans+JP:wght@400;500;700;900&display=swap" rel="stylesheet">
<style>
  :root{
    --title-yellow:#f2e21a;
    --band-yellow:#f7d90b;
    --ink:#111111;
    --accent-red:#e3211c;
    --white:#ffffff;
    --sky-mid:#6f7f95;
  }
  *{margin:0;padding:0;box-sizing:border-box}
  html,body{width:750px;height:1200px;overflow:hidden;background:#fff}
  body{font-family:"Noto Sans JP",sans-serif}
  .cover{position:relative;width:750px;height:1200px;overflow:hidden}
  .cover-backdrop{
    position:absolute;left:0;top:0;width:750px;height:862px;
    background:
      radial-gradient(ellipse 420px 190px at 375px 640px, rgba(235,240,245,.9) 0%, rgba(190,202,214,.55) 40%, rgba(120,135,155,0) 75%),
      linear-gradient(180deg, #222c3d 0%, #3b4a60 30%, var(--sky-mid) 62%, #51606f 82%, #3a4655 100%);
  }
  .title{position:absolute;left:0;width:750px;text-align:center;color:var(--title-yellow);font-weight:900;letter-spacing:4px;line-height:1;white-space:nowrap;text-shadow:0 4px 10px rgba(0,0,0,.35)}
  .title-line-1{top:70px;font-size:160px}
  .title-line-2{top:250px;font-size:200px}
  .subtitle{position:absolute;top:575px;left:0;width:750px;text-align:center;color:var(--white);font-weight:500;font-size:52px;line-height:1.2;letter-spacing:1px;white-space:nowrap;text-shadow:0 2px 6px rgba(0,0,0,.4)}
  .author{position:absolute;top:760px;left:0;width:750px;text-align:center;color:var(--white);font-weight:500;font-size:34px;line-height:1.2;letter-spacing:2px}
  .promo-band{position:absolute;left:0;top:862px;width:750px;height:338px;background:var(--band-yellow)}
  .promo-line-1{position:absolute;top:18px;left:0;width:750px;text-align:center;font-weight:900;font-size:62px;line-height:1.2;color:var(--ink);white-space:nowrap}
  .squeeze-badge{position:absolute;left:95px;top:100px;width:150px;height:150px;border-radius:50%;background:var(--white)}
  .squeeze-badge span{position:absolute;left:0;top:50px;width:150px;text-align:center;color:var(--accent-red);font-weight:900;font-size:36px;line-height:1.2;white-space:nowrap;transform:rotate(-12deg)}
  .promo-line-2{position:absolute;left:282px;top:112px;font-weight:900;font-size:50px;line-height:1.2;color:var(--ink);white-space:nowrap}
  .promo-line-2 .count{color:var(--accent-red);font-size:72px;font-style:italic;margin-right:6px}
  .gift-box{position:absolute;left:420px;top:218px;width:318px;height:112px;background:var(--white);border:3px solid var(--accent-red)}
  .gift-label{height:26px;background:var(--accent-red);color:var(--white);font-size:17px;font-weight:700;line-height:26px;text-align:center;white-space:nowrap}
  .gift-text-small{position:absolute;left:12px;top:32px;font-size:17px;font-weight:500;color:var(--ink);line-height:1.2;white-space:nowrap}
  .gift-text-large{position:absolute;left:12px;top:58px;font-size:26px;font-weight:700;color:var(--ink);line-height:1.2;white-space:nowrap}
  .gift-number{position:absolute;right:12px;top:34px;color:var(--accent-red);font-weight:900;font-size:58px;line-height:1;white-space:nowrap}
  .gift-number small{font-size:32px;color:var(--ink)}
</style>
</head>
<body>
<main class="cover">
  <div class="cover-backdrop" role="img" aria-label="薄明かりの差す海と空の風景写真"></div>
  <h1>
    <span class="title title-line-1">5つの</span>
    <span class="title title-line-2">航路</span>
  </h1>
  <p class="subtitle">ヴォルテノ大年譜など</p>
  <p class="author">RUNO</p>
  <section class="promo-band">
    <p class="promo-line-1">人類普遍の必読真理書を</p>
    <div class="squeeze-badge"><span>ギュっと</span></div>
    <p class="promo-line-2"><span class="count">1</span>冊にまとめました</p>
    <div class="gift-box">
      <p class="gift-label">●●読者限定プレゼント●●</p>
      <p class="gift-text-small">これからも成長する</p>
      <p class="gift-text-large">成功分野</p>
      <p class="gift-number">32<small>選</small></p>
    </div>
  </section>
</main>
</body>
</html>
```